Bay Bolts

I am starting a sharpening service for knives, scissors, and garden tools. It's a sole proprietorship, so it's a small business. The business name is "Bay Bolt." A one or two-page website is fine. Mark Orchard has created a logo for me. There should be pictures of the things I sharpen. There will also be a price list for sharpened items. My address is: 18302 Pellman Way, Cedar Hollow, CA 93010. Phone number is 661-555-0173

```html
<!DOCTYPE html>
<html lang="en">
<head>
<meta charset="utf-8">
<title>Bay Bolts — Precision Sharpening</title>
<link href="https://fonts.googleapis.com/css2?family=Barlow+Condensed:wght@300;400;600;700&family=Barlow:wght@400;500;600;700&display=swap" rel="stylesheet">
<style>
:root{
  --orange:#f5821f;
  --orange-soft:#f7a24e;
  --ink:#1b1b1b;
  --dark:#1f1f1f;
  --text:#3d3d3d;
  --muted:#6b6b6b;
  --line:#d9d9d9;
  --light:#f6f6f6;
  --white:#ffffff;
}
*{margin:0;padding:0;box-sizing:border-box}
html,body{width:1200px;height:4563px;overflow:hidden}
body{position:relative;background:var(--white);font-family:'Barlow',sans-serif;color:var(--text)}
.abs{position:absolute}
.heading{font-family:'Barlow Condensed',sans-serif;color:var(--ink);font-size:58px;line-height:1;text-transform:uppercase;letter-spacing:.5px}
.heading .light{font-weight:300}
.heading .bold{font-weight:700}
.rule{position:absolute;height:3px;width:70px;background:var(--orange)}
.btn{position:absolute;display:flex;align-items:center;justify-content:center;gap:8px;border-radius:30px;font-weight:600;font-size:14px;text-transform:uppercase;color:var(--white)}
.btn-orange{background:var(--orange)}
.btn-outline{border:2px solid rgba(255,255,255,.8)}
.btn-dark{background:var(--ink)}
.photo{position:absolute}

/* header */
.site-header{position:absolute;top:0;left:0;width:1200px;height:70px;background:var(--white)}
.brand{position:absolute;left:145px;top:14px;font-family:'Barlow Condensed',sans-serif;font-weight:700;font-size:30px;color:var(--ink);letter-spacing:.5px}
.nav a{position:absolute;top:27px;font-size:13px;font-weight:600;color:var(--ink);text-decoration:none;text-transform:uppercase}
.nav a.active::after{content:"";position:absolute;left:0;right:0;bottom:-8px;height:2px;background:var(--orange)}
.header-call{left:893px;top:14px;width:194px;height:41px;font-size:15px;justify-content:flex-start;padding-left:8px}
.header-call .ic{width:28px;height:28px;border-radius:50%;background:var(--white);display:flex;align-items:center;justify-content:center;margin-right:6px}

/* hero */
.hero{position:absolute;top:70px;left:0;width:1200px;height:657px;background:linear-gradient(90deg,#121212 0%,#1e1b19 35%,#5a4a3e 65%,#9a7b63 85%,#7c6a5c 100%)}
.hero .eyebrow{left:120px;top:154px;font-size:20px;letter-spacing:2px;color:var(--orange);font-weight:500}
.hero h1{left:120px;top:188px;font-family:'Barlow Condensed',sans-serif;font-weight:700;font-size:60px;line-height:62px;color:var(--white);text-transform:uppercase}
.checks{left:120px;top:325px;list-style:none}
.checks li{display:flex;align-items:center;gap:8px;color:var(--white);font-weight:600;font-size:17px;height:33.5px}
.hero-arrow{top:270px}

/* about */
.about-frame{left:96px;top:797px;width:160px;height:130px;background:var(--orange)}
.about-img1{left:110px;top:812px;width:408px;height:363px;background:linear-gradient(135deg,#7d8a8c,#1d8f8f 45%,#5b6566)}
.about-img2{left:306px;top:1001px;width:280px;height:251px;background:var(--white)}
.about-img2 div{position:absolute;inset:6px;background:linear-gradient(135deg,#9a928a,#4d4743 60%,#2b2826)}
.about-title{left:647px;top:838px}
.about p{position:absolute;left:648px;width:490px;font-size:17px;line-height:27px;color:var(--text)}

/* services band */
.band{position:absolute;left:0;top:1255px;width:1200px;height:780px}
.band-title{left:0;width:1200px;top:1432px;text-align:center;color:var(--white)}
.band-title .heading{color:var(--white)}
.svc{position:absolute;top:1533px;width:327px;height:341px;background:#111;border:1px solid #444}
.svc .photo{left:0;top:0;width:325px;height:239px}
.svc h3{position:absolute;left:0;right:0;top:261px;text-align:center;color:var(--white);font-size:20px;font-weight:700;text-transform:uppercase}
.svc p{position:absolute;left:0;right:0;top:293px;text-align:center;color:#ddd;font-size:14px}

/* how it works */
.how-title{left:0;width:1200px;top:2024px;text-align:center}
.how-sub{left:0;width:1200px;top:2111px;text-align:center;font-size:17px;color:var(--ink)}
.step{position:absolute;width:294px;height:294px;top:2189px;text-align:center}
.step .ring{position:absolute;inset:0;border-radius:50%;background:var(--white);box-shadow:0 0 0 1px #e3e3e3}
.step .icon{position:absolute;left:117px;top:52px}
.step h4{position:absolute;left:0;right:0;top:146px;font-size:18px;font-weight:600;color:var(--ink)}
.step p{position:absolute;left:70px;right:70px;top:175px;font-size:15px;line-height:20px;color:var(--muted)}
.step .num{position:absolute;left:127px;top:256px;width:40px;height:40px;border-radius:50%;background:var(--orange);color:var(--white);font-size:15px;display:flex;align-items:center;justify-content:center;border:3px solid #fbd3ad}

/* pricing */
.pricing-bg{left:0;top:2561px;width:1200px;height:640px;background:var(--light)}
.price-card{left:96px;top:2646px;width:507px;height:477px;background:var(--white)}
.price-img{left:603px;top:2646px;width:480px;height:477px;background:linear-gradient(135deg,#2a5f9e 0%,#5a3a22 25%,#7a4f2d 55%,#4e3019 100%)}
.price-title{left:160px;top:2700px;font-size:54px}
.price-intro{left:160px;top:2786px;width:380px;font-size:15.5px;line-height:20px;color:var(--muted)}
.price-row{position:absolute;left:160px;width:376px;height:53px;display:flex;align-items:center;border-bottom:1px solid #bfbfbf}
.price-row.last{border-bottom:none}
.price-row .ic{width:38px;display:flex;justify-content:center;margin-right:14px}
.price-row .label{flex:1;font-size:19px;color:var(--ink)}
.price-row .price{font-size:20px;font-weight:700;color:var(--ink);width:70px}

/* reviews */
.reviews-title{left:0;width:1200px;top:3236px;text-align:center}
.review{position:absolute;top:3339px;width:300px;height:237px;border:2px solid #e3e3e3;background:var(--white);padding:34px 36px}
.stars{color:var(--orange);font-size:20px;letter-spacing:2px;line-height:20px}
.review p{margin-top:12px;font-size:13.5px;line-height:22px;color:var(--text)}
.review .name{margin-top:10px;font-weight:700;font-size:14px;color:var(--ink)}
.rev-arrow{position:absolute;top:3475px;width:42px;height:42px;border-radius:50%;background:var(--white);box-shadow:0 2px 8px rgba(0,0,0,.15);display:flex;align-items:center;justify-content:center}

/* contact */
.footer{left:0;top:4139px;width:1200px;height:424px;background:var(--dark)}
.contact-card{left:94px;top:3692px;width:1032px;height:544px;background:linear-gradient(90deg,#f58a26 0%,#f38320 60%,#e87a1e 100%);border-radius:4px}
.map{left:190px;top:3772px;width:390px;height:390px;border-radius:50%;background:radial-gradient(circle,#f2f2f2 0%,#dcdcdc 100%);border:6px solid var(--white);box-shadow:0 0 0 4px rgba(255,255,255,.35)}
.contact-eyebrow{left:619px;top:3792px;font-size:15px;letter-spacing:2px;color:var(--white);font-weight:600}
.contact-title{left:619px;top:3812px;font-size:54px;color:var(--white)}
.contact-item{position:absolute;left:619px;display:flex;gap:18px;align-items:flex-start}
.contact-item .pin{width:38px;height:38px;border-radius:50%;background:var(--white);display:flex;align-items:center;justify-content:center;margin-top:4px}
.contact-item .lbl{font-size:19px;color:var(--white)}
.contact-item .val{font-size:18px;font-weight:700;color:var(--white);line-height:23px}
.contact-call{left:613px;top:4084px;width:215px;height:54px;font-size:18px}

/* footer */
.foot-brand{left:172px;top:4296px;font-family:'Barlow Condensed',sans-serif;font-weight:700;font-size:40px;color:var(--white);letter-spacing:.5px}
.foot-nav{position:absolute;top:4312px;left:0;width:1200px}
.foot-nav a{position:absolute;color:var(--white);font-weight:600;font-size:15px;text-decoration:none;text-transform:uppercase}
.foot-nav i{position:absolute;top:8px;width:5px;height:5px;border-radius:50%;background:var(--orange)}
.foot-rule{left:163px;width:874px;height:1px;background:#3e3e3e}
.foot-item{position:absolute;top:4426px;display:flex;align-items:center;gap:12px;color:var(--white)}
.foot-item .ic{width:30px;height:30px;border-radius:50%;background:var(--white);display:flex;align-items:center;justify-content:center}
.foot-item small{display:block;font-size:13px;line-height:16px}
.foot-item b{display:block;font-size:13px;font-weight:600;line-height:16px}
.social{position:absolute;top:4432px;width:28px;height:28px;border-radius:50%}
.copyright{left:0;width:1200px;top:4521px;text-align:center;font-size:12px;color:#9a9a9a}
</style>
</head>
<body>

<header class="site-header">
  <div class="brand">BAY BOLTS</div>
  <nav class="nav">
    <a class="active" style="left:372px">Home</a>
    <a style="left:459px">About Us</a>
    <a style="left:574px">Services</a>
    <a style="left:686px">Pricing</a>
    <a style="left:790px">Contact</a>
  </nav>
  <div class="btn btn-orange header-call"><span class="ic"><svg width="14" height="14" viewBox="0 0 24 24"><path fill="#f5821f" d="M6.6 10.8a15.1 15.1 0 0 0 6.6 6.6l2.2-2.2a1 1 0 0 1 1-.25 11.4 11.4 0 0 0 3.6.57 1 1 0 0 1 1 1V20a1 1 0 0 1-1 1A17 17 0 0 1 3 4a1 1 0 0 1 1-1h3.5a1 1 0 0 1 1 1c0 1.25.2 2.45.57 3.57a1 1 0 0 1-.25 1z"/></svg></span>661-555-0173</div>
</header>

<section class="hero">
  <div class="photo" role="img" aria-label="Hands sharpening a blade against a spinning grinding wheel with sparks" style="inset:0"></div>
  <div class="abs eyebrow">WELCOME TO BAY BOLTS</div>
  <h1 class="abs">Precision Sharpening<br>Professional Results</h1>
  <ul class="abs checks">
    <li><svg width="16" height="14" viewBox="0 0 16 14"><path d="M1 7l5 5 9-11" fill="none" stroke="#f5821f" stroke-width="2.5"/></svg>Precision Sharpening</li>
    <li><svg width="16" height="14" viewBox="0 0 16 14"><path d="M1 7l5 5 9-11" fill="none" stroke="#f5821f" stroke-width="2.5"/></svg>Affordable pricing</li>
    <li><svg width="16" height="14" viewBox="0 0 16 14"><path d="M1 7l5 5 9-11" fill="none" stroke="#f5821f" stroke-width="2.5"/></svg>Local &amp; reliable service</li>
  </ul>
  <div class="btn btn-outline" style="left:120px;top:442px;width:181px;height:50px">View Prices <svg width="14" height="12" viewBox="0 0 14 12"><path d="M0 6h12M7 1l5 5-5 5" fill="none" stroke="#fff" stroke-width="2"/></svg></div>
  <div class="btn btn-orange" style="left:308px;top:442px;width:181px;height:50px">Call Us Now <svg width="14" height="12" viewBox="0 0 14 12"><path d="M0 6h12M7 1l5 5-5 5" fill="none" stroke="#fff" stroke-width="2"/></svg></div>
  <svg class="abs hero-arrow" style="left:34px" width="20" height="32" viewBox="0 0 20 32"><path d="M16 3L4 16l12 13" fill="none" stroke="#fff" stroke-width="3"/></svg>
  <svg class="abs hero-arrow" style="left:1144px" width="20" height="32" viewBox="0 0 20 32"><path d="M4 3l12 13L4 29" fill="none" stroke="#fff" stroke-width="3"/></svg>
</section>

<section class="about">
  <div class="abs about-frame"></div>
  <div class="photo about-img1" role="img" aria-label="Blade being sharpened on a teal bench grinder"></div>
  <div class="photo about-img2" role="img" aria-label="Hand holding a tool against a grinding disc"><div></div></div>
  <h2 class="abs heading about-title"><span class="light">About</span> <span class="bold">Bay Bolts</span></h2>
  <div class="rule" style="left:648px;top:905px"></div>
  <p style="top:934px">Lorem ipsum dolor sit amet, consectetur adipiscing elit, sed do eiusmod tempor incididunt ut labore et dolore magna aliqua. Quis ipsum suspendisse ultrices gravida. Risus commodo viverra maecenas accumsan lacus vel facilisis.</p>
  <p style="top:1071px">Lorem ipsum dolor sit amet, consectetur adipiscing elit, sed do eiusmod tempor incididunt ut labore et dolore</p>
  <div class="btn btn-orange" style="left:647px;top:1156px;width:180px;height:46px">Call Us Now <svg width="14" height="12" viewBox="0 0 14 12"><path d="M0 6h12M7 1l5 5-5 5" fill="none" stroke="#fff" stroke-width="2"/></svg></div>
</section>

<section>
  <svg class="band" viewBox="0 0 1200 780" role="img" aria-label="Dark workshop backdrop with angled orange bands">
    <defs><linearGradient id="bandShade" x1="0" y1="0" x2="1" y2="0"><stop offset="0" stop-color="#262626"/><stop offset=".5" stop-color="#2e2e2e"/><stop offset="1" stop-color="#1e1e1e"/></linearGradient></defs>
    <polygon points="0,92 1200,7 1200,668 0,766" fill="url(#bandShade)"/>
    <polygon points="0,92 330,69 0,137" fill="#f5821f"/>
    <polygon points="1200,640 1200,678 870,703" fill="#f5821f"/>
  </svg>
  <div class="abs band-title"><h2 class="heading"><span class="light">What We</span> <span class="bold">Sharpen</span></h2></div>
  <div class="rule" style="left:565px;top:1500px"></div>
  <div class="svc" style="left:94px"><div class="photo" role="img" aria-label="Three kitchen knives standing on a wooden board" style="background:linear-gradient(135deg,#8a5a32,#3b2a1e 50%,#6e4628)"></div><h3>Knives</h3><p>Kitchen, chef, hunting, pocket knives</p></div>
  <div class="svc" style="left:436px"><div class="photo" role="img" aria-label="Scissors being sharpened on a grinding wheel with sparks" style="background:linear-gradient(135deg,#5d5048,#a08672 45%,#2b2522)"></div><h3>Scissors Sharpening</h3><p>Household, salon, fabric, utility</p></div>
  <div class="svc" style="left:776px"><div class="photo" role="img" aria-label="Garden pruning shears clamped for sharpening" style="background:linear-gradient(135deg,#3c3c3c,#8a8a86 50%,#2a2a2a)"></div><h3>Garden Tools</h3><p>Shears, pruners, loppers, hedge tools</p></div>
</section>

<section>
  <h2 class="abs heading how-title"><span class="light">How It</span> <span class="bold">Works</span></h2>
  <div class="rule" style="left:565px;top:2091px"></div>
  <p class="abs how-sub">Lorem ipsum dolor sit amet, consectetur adipiscing elit, sed do eiusmod tempor inc</p>

  <svg class="abs" style="left:0;top:2160px" width="1200" height="360" viewBox="0 0 1200 360">
    <g fill="none" stroke="#cfcfcf" stroke-width="7" stroke-linecap="round">
      <path d="M163 260 A147 147 0 0 1 366 45"/>
      <path d="M493 80 A147 147 0 0 1 759 120"/>
      <path d="M1082 112 A147 147 0 0 1 860 300"/>
    </g>
    <g fill="none" stroke="#8f8f8f" stroke-width="1.5">
      <path d="M422 168 Q460 185 496 160"/><path d="M488 156 l8 4 -4 8"/>
      <path d="M740 162 Q775 140 812 160"/><path d="M804 154 l8 6 -7 7"/>
    </g>
  </svg>

  <div class="step" style="left:145px"><div class="ring"></div>
    <svg class="icon" width="60" height="60" viewBox="0 0 60 60" fill="none" stroke="#f5821f" stroke-width="2.5"><path d="M16 10l8 10-5 5a30 30 0 0 0 16 16l5-5 10 8-6 8c-20 0-36-16-36-36z"/><path d="M34 14a14 14 0 0 1 12 12M34 6a22 22 0 0 1 20 20"/></svg>
    <h4>Drop off or contact us</h4><p>Lorem ipsum dolor sit amet consectetur</p><div class="num">01</div></div>
  <div class="step" style="left:473px"><div class="ring"></div>
    <svg class="icon" width="60" height="60" viewBox="0 0 60 60" fill="none" stroke="#f5821f" stroke-width="2.5"><circle cx="34" cy="34" r="20"/><circle cx="34" cy="34" r="8"/><path d="M6 40L30 14M10 44l-4 4"/></svg>
    <h4>We sharpen your tools</h4><p>Lorem ipsum dolor sit amet consectetur</p><div class="num">02</div></div>
  <div class="step" style="left:792px"><div class="ring"></div>
    <svg class="icon" width="60" height="60" viewBox="0 0 60 60" fill="none" stroke="#f5821f" stroke-width="2.5"><path d="M50 6L22 38l6 6L54 12z"/><path d="M22 38l-12 12a4 4 0 0 0 6 6l12-12"/></svg>
    <h4>Pick up sharp results</h4><p>Lorem ipsum dolor sit amet consectetur</p><div class="num">03</div></div>
</section>

<section>
  <div class="abs pricing-bg"></div>
  <div class="abs price-card"></div>
  <div class="photo price-img" role="img" aria-label="Knives and scissors laid out on a dark wooden table"></div>
  <h2 class="abs heading price-title"><span class="light">Our</span> <span class="bold">Pricing</span></h2>
  <div class="rule" style="left:160px;top:2761px"></div>
  <p class="abs price-intro">Lorem ipsum dolor sit amet, consectetur adipiscing elit, sed do eiusmod tempor incididunt</p>
  <div class="price-row" style="top:2850px"><span class="ic"><svg width="30" height="30" viewBox="0 0 30 30"><path d="M3 4l18 18 3-2L6 3z" fill="#222"/><path d="M21 22l5 5" stroke="#222" stroke-width="3"/></svg></span><span class="label">Standard Knife</span><span class="price">$15</span></div>
  <div class="price-row" style="top:2903px"><span class="ic"><svg width="30" height="30" viewBox="0 0 30 30"><path d="M27 2L10 20l3 3L29 5z" fill="#222"/><path d="M10 20l-7 7" stroke="#222" stroke-width="3"/></svg></span><span class="label">Large Knife</span><span class="price">$25</span></div>
  <div class="price-row" style="top:2956px"><span class="ic"><svg width="30" height="30" viewBox="0 0 30 30" fill="none" stroke="#222" stroke-width="2"><circle cx="7" cy="24" r="3.5"/><circle cx="13" cy="27" r="2.5"/><path d="M9 21L26 3M12 25L20 10"/></svg></span><span class="label">Scissors</span><span class="price">$10</span></div>
  <div class="price-row last" style="top:3009px"><span class="ic"><svg width="30" height="30" viewBox="0 0 30 30" fill="none" stroke="#222" stroke-width="2"><path d="M4 26l9-9M6 20l7 1M15 15l12-11M15 15c4-1 8 0 10 3"/></svg></span><span class="label">Garden Tools</span><span class="price">$30</span></div>
</section>

<section>
  <h2 class="abs heading reviews-title"><span class="bold">Reviews</span></h2>
  <div class="rule" style="left:565px;top:3303px"></div>
  <div class="rev-arrow" style="left:64px"><svg width="16" height="12" viewBox="0 0 16 12"><path d="M16 6H2M6 1L1 6l5 5" fill="none" stroke="#333" stroke-width="1.5"/></svg></div>
  <div class="review" style="left:135px"><div class="stars">★★★★★</div><p>"Lorem ipsum dolor sit amet, consectetur adipiscing elit, sed do eiusmod tempor incididunt ut labore et dolore magna aliqua Ut enim ad minim veniam, quis nostrud"</p><div class="name">Dana Reyes</div></div>
  <div class="review" style="left:454px"><div class="stars">★★★★★</div><p>"Lorem ipsum dolor sit amet, consectetur adipiscing elit, sed do eiusmod tempor incididunt ut labore et dolore magna aliqua Ut enim ad minim veniam, quis nostrud"</p><div class="name">Dana Reyes</div></div>
  <div class="review" style="left:773px"><div class="stars">★★★★★</div><p>"Lorem ipsum dolor sit amet, consectetur adipiscing elit, sed do eiusmod tempor incididunt ut labore et dolore magna aliqua Ut enim ad minim veniam, quis nostrud"</p><div class="name">Dana Reyes</div></div>
  <div class="rev-arrow" style="left:1116px"><svg width="16" height="12" viewBox="0 0 16 12"><path d="M0 6h14M10 1l5 5-5 5" fill="none" stroke="#333" stroke-width="1.5"/></svg></div>
</section>

<footer>
  <div class="abs footer"></div>
  <div class="abs contact-card" role="img" aria-label="Orange tinted photo of a blade being sharpened"></div>
  <div class="abs map" role="img" aria-label="Street map of the neighborhood showing the shop location"></div>
  <div class="abs contact-eyebrow">GET IN TOUCH</div>
  <h2 class="abs heading contact-title"><span class="bold">Contact Us</span></h2>
  <div class="contact-item" style="top:3905px"><span class="pin"><svg width="16" height="20" viewBox="0 0 16 20"><path d="M8 0a8 8 0 0 0-8 8c0 6 8 12 8 12s8-6 8-12a8 8 0 0 0-8-8z" fill="#f5821f"/><circle cx="8" cy="8" r="3" fill="#fff"/></svg></span><div><div class="lbl">Address</div><div class="val">18302 Pellman Way, Cedar<br>Hollow, CA 93010</div></div></div>
  <div class="contact-item" style="top:4006px"><span class="pin"><svg width="16" height="16" viewBox="0 0 24 24"><path fill="#f5821f" d="M6.6 10.8a15.1 15.1 0 0 0 6.6 6.6l2.2-2.2a1 1 0 0 1 1-.25 11.4 11.4 0 0 0 3.6.57 1 1 0 0 1 1 1V20a1 1 0 0 1-1 1A17 17 0 0 1 3 4a1 1 0 0 1 1-1h3.5a1 1 0 0 1 1 1c0 1.25.2 2.45.57 3.57a1 1 0 0 1-.25 1z"/></svg></span><div><div class="lbl">Phone Number</div><div class="val">661-555-0173</div></div></div>
  <div class="btn btn-dark contact-call">Call Us Now <svg width="16" height="12" viewBox="0 0 16 12"><path d="M0 6h14M9 1l5 5-5 5" fill="none" stroke="#fff" stroke-width="2"/></svg></div>

  <div class="abs foot-brand">BAY BOLTS</div>
  <nav class="foot-nav">
    <a style="left:399px">Home</a><i style="left:477px"></i>
    <a style="left:512px">About Us</a><i style="left:622px"></i>
    <a style="left:658px">Services</a><i style="left:762px"></i>
    <a style="left:799px">Pricing</a><i style="left:899px"></i>
    <a style="left:934px">Contact</a>
  </nav>
  <div class="abs foot-rule" style="top:4399px"></div>
  <div class="foot-item" style="left:228px"><span class="ic"><svg width="14" height="14" viewBox="0 0 24 24"><path fill="#1f1f1f" d="M6.6 10.8a15.1 15.1 0 0 0 6.6 6.6l2.2-2.2a1 1 0 0 1 1-.25 11.4 11.4 0 0 0 3.6.57 1 1 0 0 1 1 1V20a1 1 0 0 1-1 1A17 17 0 0 1 3 4a1 1 0 0 1 1-1h3.5a1 1 0 0 1 1 1c0 1.25.2 2.45.57 3.57a1 1 0 0 1-.25 1z"/></svg></span><div><small>Phone Number</small><b>661-555-0173</b></div></div>
  <div class="foot-item" style="left:460px"><span class="ic"><svg width="14" height="18" viewBox="0 0 16 20"><path d="M8 0a8 8 0 0 0-8 8c0 6 8 12 8 12s8-6 8-12a8 8 0 0 0-8-8z" fill="#1f1f1f"/><circle cx="8" cy="8" r="3" fill="#fff"/></svg></span><div><small>Address</small><b>18302 Pellman Way, Cedar Hollow, CA 93010</b></div></div>
  <span class="social" style="left:920px;background:var(--orange)"></span>
  <span class="social" style="left:954px;background:var(--white)"></span>
  <span class="social" style="left:988px;background:var(--white)"></span>
  <div class="abs foot-rule" style="top:4493px"></div>
  <div class="abs copyright">© 2026 Bay Bolts. All Rights Reserved</div>
</footer>

</body>
</html>
```